Torvane PT Business Card

I need the card to be bright/bold colours to stand out amongst others.
It needs to have my company logo.
I was not interested in pictures etc just a layout that attracts attention.

I have attached my old design which is very plain. I also needed change the contact details. And my description changed to Personal Trainer
Phone 0427309581
Facebook Torvane PT
No email address please, no street address.
And only Torvane PT (Please remove anything to do with Torvane Supplements)

```html
<!DOCTYPE html>
<html lang="en">
<head>
<meta charset="utf-8">
<title>Torvane PT Business Card</title>
<link rel="stylesheet" href="https://fonts.googleapis.com/css2?family=Lato:wght@400;700;900&display=swap">
<style>
  :root {
    --backdrop: #1b1b1c;
    --card: #262627;
    --card-edge: #303031;
    --brand-blue: #1b72a8;
    --brand-blue-bright: #2289c6;
    --brand-yellow: #f2d41c;
    --icon-yellow: #d9b914;
  }
  * { box-sizing: border-box; margin: 0; padding: 0; }
  html, body {
    width: 1200px;
    height: 997px;
    overflow: hidden;
    background: var(--backdrop);
    font-family: "Lato", Arial, sans-serif;
  }
  .card {
    position: absolute;
    left: 150px;
    top: 238px;
    width: 900px;
    height: 520px;
    border-radius: 30px;
    background: linear-gradient(160deg, var(--card-edge), var(--card) 45%);
    overflow: hidden;
    box-shadow: 0 18px 40px rgba(0,0,0,.55);
  }
  .brand {
    position: absolute;
    left: 130px;
    top: 62px;
    width: 500px;
    text-align: center;
    white-space: nowrap;
  }
  .brand-name {
    font-weight: 900;
    font-size: 64px;
    letter-spacing: 2px;
    color: var(--brand-yellow);
    line-height: 1;
  }
  .brand-rule {
    position: absolute;
    left: 160px;
    top: 142px;
    width: 440px;
    height: 2px;
    background: var(--brand-blue-bright);
  }
  .divider {
    position: absolute;
    left: 470px;
    top: 185px;
    width: 3px;
    height: 160px;
    background: linear-gradient(180deg, transparent, var(--brand-blue-bright) 50%, transparent);
  }
  .person {
    position: absolute;
    left: 80px;
    top: 262px;
    white-space: nowrap;
  }
  .person-name {
    font-weight: 700;
    font-size: 30px;
    letter-spacing: 1px;
    color: var(--brand-blue-bright);
    text-transform: uppercase;
  }
  .person-role {
    margin-top: 4px;
    padding-left: 34px;
    font-weight: 700;
    font-size: 19px;
    color: var(--brand-yellow);
  }
  .contacts {
    position: absolute;
    left: 520px;
    top: 222px;
    list-style: none;
    white-space: nowrap;
  }
  .contact {
    display: flex;
    align-items: center;
    gap: 14px;
    margin-bottom: 20px;
    font-size: 22px;
    line-height: 1.2;
    letter-spacing: .5px;
    color: var(--brand-blue-bright);
  }
  .contact-icon {
    flex: none;
    width: 22px;
    height: 22px;
  }
  .web-band {
    position: absolute;
    left: 0;
    bottom: 0;
    width: 100%;
    height: 92px;
    background: var(--brand-blue);
  }
</style>
</head>
<body>
  <div class="card">
    <div class="brand"><div class="brand-name">TORVANE PT</div></div>
    <div class="brand-rule"></div>

    <div class="person">
      <div class="person-name">Dana Mercer</div>
      <div class="person-role">Personal Trainer</div>
    </div>

    <div class="divider"></div>

    <ul class="contacts">
      <li class="contact">
        <svg class="contact-icon" viewBox="0 0 22 22" aria-hidden="true">
          <circle cx="11" cy="11" r="11" fill="var(--icon-yellow)"/>
          <path d="M5 9c0-2 2-3 6-3s6 1 6 3l-2 1-1-2H8l-1 2z M7 11h8l1 5H6z" fill="#262627"/>
        </svg>
        <span>0427309581</span>
      </li>
      <li class="contact">
        <svg class="contact-icon" viewBox="0 0 22 22" aria-hidden="true">
          <circle cx="11" cy="11" r="11" fill="var(--icon-yellow)"/>
        </svg>
        <span>Torvane PT</span>
      </li>
    </ul>

    <div class="web-band"></div>
  </div>
</body>
</html>
```